Business Card Design

We are a manufacturing company that has been in business for over 30 years, established in 1981. We are looking to increase our business with defence force, government, and the major telecoms so the card needs to present the company as being cutting edge, secure, and professional.
Industry/Entity Type
Defence
Contact Information for Business Card
Name Gareth Olsund
Phone 02 9374 6815
Fax 02 9457 3162
mobile 0438260517
Email Gary@Korvex.com.au
Webiste www.korvex.com.au
ABN 58 006 391 842
address: 17 Belcor Street Ingleburn NSW 2565
"Manufacturer of Antennas, GPS, Microwave, Cable Assemblies, RF, Military, & Telecommunications"
Look and feel

```html
<!DOCTYPE html>
<html lang="en">
<head>
<meta charset="utf-8">
<title>Korvex Business Card</title>
<link href="https://fonts.googleapis.com/css2?family=Open+Sans:wght@400;700&family=Questrial&display=swap" rel="stylesheet">
<style>
  :root {
    --navy: #16214f;
    --red: #b83a24;
    --white: #ffffff;
    --paper: #ffffff;
    --backdrop: #e9e6e1;
  }
  * { margin: 0; padding: 0; box-sizing: border-box; }
  html, body { width: 1200px; height: 1019px; overflow: hidden; }
  body {
    background: var(--backdrop);
    position: relative;
    font-family: "Open Sans", sans-serif;
  }
  .card {
    position: absolute;
    top: 200px;
    width: 380px;
    height: 620px;
    overflow: hidden;
    box-shadow: 0 6px 18px rgba(0,0,0,0.18);
  }
  .card--front { left: 170px; background: var(--red); }
  .card--back  { left: 650px; background: var(--paper); }

  /* Front */
  .front__top {
    position: absolute; left: 0; top: 0;
    width: 100%; height: 330px;
    background: var(--navy);
    border-bottom: 5px solid var(--white);
  }
  .front__brand {
    position: absolute; left: 34px; top: 40px;
    font-family: "Questrial", sans-serif;
    font-size: 46px;
    letter-spacing: 6px;
    color: var(--white);
  }
  .front__name {
    position: absolute; right: 34px; bottom: 22px;
    font-family: "Questrial", sans-serif;
    font-size: 28px;
    color: var(--white);
  }
  .front__contact {
    position: absolute; left: 40px; top: 362px;
    color: var(--white);
    font-size: 17px;
    line-height: 1.32;
  }
  .front__contact .label { font-weight: 700; }
  .front__contact .web { font-weight: 700; }
  .front__address { margin-top: 14px; }
  .front__abn { margin-top: 12px; }

  /* Back */
  .back__mark {
    position: absolute; left: 60px; top: 70px;
    width: 260px;
  }
  .back__square {
    width: 260px; height: 150px;
    background: var(--navy);
  }
  .back__band {
    margin-top: 6px;
    height: 56px;
    background: var(--red);
    display: flex; align-items: center; justify-content: center;
    font-family: "Questrial", sans-serif;
    font-size: 30px;
    letter-spacing: 8px;
    color: var(--white);
  }
  .back__tagline {
    position: absolute; left: 20px; right: 20px; bottom: 54px;
    text-align: center;
    font-family: "Questrial", sans-serif;
    font-size: 17px;
    line-height: 1.3;
    color: var(--navy);
  }
</style>
</head>
<body>
  <section class="card card--front">
    <div class="front__top">
      <div class="front__brand">KORVEX</div>
      <div class="front__name">Gareth Olsund</div>
    </div>
    <div class="front__contact">
      <p><span class="label">Phone</span> 02 9374 6815</p>
      <p><span class="label">Fax</span> 02 9457 3162</p>
      <p><span class="label">Mobile</span> 0438260517</p>
      <p>Gary@Korvex.com.au</p>
      <p class="web">www.korvex.com.au</p>
      <p class="front__address">17 Belcor Street<br>Tallowmere NSW 2574</p>
      <p class="front__abn">ABN 58 006 391 842</p>
    </div>
  </section>

  <section class="card card--back">
    <div class="back__mark">
      <div class="back__square"></div>
      <div class="back__band">KORVEX</div>
    </div>
    <p class="back__tagline">
      Manufacturer of<br>
      Antennas, GPS, Microwave,<br>
      Cable Assemblies, RF,<br>
      Military, &amp; Telecommunications
    </p>
  </section>
</body>
</html>
```